Flyer for my live dj set from a recent party (party flyer included)

Need a recreation of a flyer for my live dj mix from the night of the party

(I added a pic of me and my logo if that looks good as well):

TEXT:

NO SLEEPING UNDER THE MIRROR BALL

VELTRA PRODUCTIONS One Year Anniversary Party 2019

MORVIN (Closing Set)

Recorded Live at Redgate Hollow Brewery

linkspace.net/morvin482

Target Market(s)

Electronic Music, Nightclub goers

Industry/Entity Type

Night Club

Font styles to use
Sans Serif

Colors

Designer to choose colors to be used in the design.

Requirements
Must have
• Elements of the original party flyer
Nice to have
• Some bright or neon, something that pops. Try to keep it similar to the flyer attached so it has the same theme and looks like a promo mix for that party

```html
<!DOCTYPE html>
<html lang="en">
<head>
<meta charset="utf-8">
<title>Veltra Productions – One Year Anniversary Party 2019 – Morvin Closing Set</title>
<link rel="stylesheet" href="https://fonts.googleapis.com/css2?family=Michroma&family=Russo+One&family=Poppins:wght@400;500&display=swap">
<style>
  :root {
    --stage: #1f1f1f;
    --indigo-deep: #1c1470;
    --indigo: #2f23a8;
    --violet: #5a2bb8;
    --magenta: #d0246f;
    --pink: #ff3d8c;
    --white: #ffffff;
    --shadow: rgba(10, 4, 40, 0.55);
  }
  html, body {
    margin: 0;
    width: 1200px;
    height: 1200px;
    overflow: hidden;
    background: var(--stage);
  }
  .flyer {
    position: absolute;
    left: 210px;
    top: 95px;
    width: 780px;
    height: 1010px;
    overflow: hidden;
    color: var(--white);
    font-family: "Michroma", sans-serif;
    background:
      linear-gradient(125deg, rgba(255,61,140,0) 35%, rgba(255,61,140,0.35) 60%, rgba(208,36,111,0.6) 100%),
      linear-gradient(180deg, var(--indigo-deep) 0%, var(--indigo) 35%, var(--violet) 70%, var(--magenta) 100%);
  }
  .headline-band {
    position: absolute;
    left: 0; top: 66px;
    width: 100%; height: 79px;
    background: linear-gradient(90deg, var(--indigo-deep) 0%, var(--violet) 45%, var(--magenta) 100%);
    display: flex; align-items: center; justify-content: center;
    font-size: 21px;
    letter-spacing: 0.5px;
  }
  .presenter {
    position: absolute; top: 180px; width: 100%;
    text-align: center; font-size: 17px;
  }
  .event-title {
    position: absolute; top: 215px; width: 100%;
    margin: 0; text-align: center; font-weight: 400;
    text-shadow: 0 4px 6px var(--shadow);
  }
  .event-title span { display: block; }
  .event-title .line-one { font-size: 58px; line-height: 64px; }
  .event-title .line-two { font-size: 56px; line-height: 66px; }
  .event-title .line-three { font-size: 92px; line-height: 104px; }
  .year-ribbon {
    position: absolute; left: 111px; top: 476px;
    width: 555px; height: 74px;
  }
  .year-ribbon svg { position: absolute; inset: 0; }
  .year-ribbon .year {
    position: absolute; inset: 0;
    display: flex; align-items: center; justify-content: center;
    font-size: 60px; letter-spacing: 10px;
    text-shadow: 0 3px 5px var(--shadow);
  }
  .accent-ring {
    position: absolute; left: 35px; top: 581px;
    width: 62px; height: 62px;
    border: 2px solid var(--pink); border-radius: 50%;
  }
  .artist-photo {
    position: absolute; left: 53px; top: 551px;
    width: 280px; height: 280px; border-radius: 50%;
    border: 4px solid var(--magenta);
    background: radial-gradient(circle at 45% 40%, #a0303e 0%, #4a1a55 45%, #1a1240 100%);
  }
  .love-house {
    position: absolute; left: 440px; top: 615px;
    width: 250px; height: 60px;
  }
  .artist-name {
    position: absolute; left: 285px; top: 738px;
    width: 430px; text-align: center;
    font-family: "Russo One", sans-serif;
    font-size: 86px; line-height: 90px;
    letter-spacing: 2px;
    text-shadow: 0 4px 6px var(--shadow);
  }
  .set-label {
    position: absolute; left: 285px; top: 832px;
    width: 430px; text-align: center; font-size: 16px;
  }
  .social {
    position: absolute; left: 235px; top: 898px;
    display: flex; align-items: center; gap: 12px;
    font-family: "Poppins", sans-serif; font-size: 19px;
  }
  .social .dot {
    width: 30px; height: 30px; border-radius: 50%;
    background: var(--white);
  }
  .venue-line {
    position: absolute; left: 170px; top: 942px;
    width: 420px; text-align: center;
    font-family: "Poppins", sans-serif; font-size: 18px;
  }
  .venue-mark {
    position: absolute; left: 563px; top: 871px;
    width: 120px; height: 120px; border-radius: 50%;
    background: var(--indigo-deep);
    border: 3px solid var(--white);
    display: flex; align-items: center; justify-content: center;
    text-align: center;
    font-size: 11px; line-height: 16px;
  }
</style>
</head>
<body>
  <main class="flyer">
    <div class="headline-band">NO SLEEPING UNDER THE MIRROR BALL</div>
    <div class="presenter">VELTRA PRODUCTIONS</div>
    <h1 class="event-title">
      <span class="line-one">ONE YEAR</span>
      <span class="line-two">ANNIVERSARY</span>
      <span class="line-three">PARTY</span>
    </h1>
    <div class="year-ribbon">
      <svg width="555" height="74" viewBox="0 0 555 74">
        <defs>
          <linearGradient id="ribbonFill" x1="0" x2="1" y1="0" y2="0">
            <stop offset="0" stop-color="#2a1a9a"/>
            <stop offset="0.5" stop-color="#7a2aa8"/>
            <stop offset="1" stop-color="#e02a78"/>
          </linearGradient>
        </defs>
        <polygon points="8,12 555,0 548,68 0,74" fill="url(#ribbonFill)"/>
      </svg>
      <div class="year">2019</div>
    </div>
    <div class="accent-ring"></div>
    <div class="artist-photo" role="img" aria-label="Photo of the DJ performing at the decks"></div>
    <svg class="love-house" viewBox="0 0 250 60" aria-label="I love house music">
      <text x="0" y="48" font-family="Poppins, sans-serif" font-size="46" fill="#ffffff">I</text>
      <path d="M68 22 C68 10 84 8 88 20 C92 8 108 10 108 22 C108 34 88 46 88 46 C88 46 68 34 68 22 Z" fill="none" stroke="#e8203a" stroke-width="3"/>
      <path d="M140 30 L160 14 L180 30 M146 26 V46 H174 V26 M156 46 V36 H164 V46" fill="none" stroke="#ffffff" stroke-width="2.5" stroke-linejoin="round"/>
      <path d="M212 40 V16 L234 12 V36" fill="none" stroke="#ffffff" stroke-width="3"/>
      <ellipse cx="208" cy="41" rx="6" ry="5" fill="#ffffff"/>
      <ellipse cx="230" cy="37" rx="6" ry="5" fill="#ffffff"/>
    </svg>
    <div class="artist-name">MORVIN</div>
    <div class="set-label">CLOSING SET</div>
    <div class="social"><span class="dot"></span>linkspace.net/morvin482</div>
    <div class="venue-line">Recorded Live at Redgate Hollow Brewery</div>
    <div class="venue-mark">REDGATE<br>HOLLOW<br>BREWERY</div>
  </main>
</body>
</html>
```